The Bright Path Foundation

This is a non profit . We are a 501(c)(3) charitable organization in the United States. The organization is a volunteer based group providing basic healthcare to those living in underserved rural areas around the world. I have attached a brochure that provides some information about the organization. We are looking for a basic 5 page web page Page 1 Photos that fade into the next x 3 with mission statementPage 2 About us - details about bright path foundation. also introducing our Founders of the organization. Marlene Quist, M.D. Doria Lemke , FNP, Paula Dweck, FNP, Brent Lomax. ( will provide you info on each.Page 3 Projects coming up and futurePage 4 Get involved - Give a donation, Volunteer, Corporate supportPage 5 Support us and contact us with a message box.We mainly work in South America but anticipate trave to South Africa in the near future. Colors bright with emphasis on Reds and Purples. I have attached some photos and ideas. You can use or not use ok to use something similar if you so like

Target Market(s)

People interested in volunteering time or money to overseas medical work. NOT a religious base

Colors
876aae
ec1f27
f37022
9bcb3c

Requirements
Must have
• Colorful pictures nature, brings out emotion, colorful, children from various parts of the world, animals.
• Tried to down load some pictures but would not go thru.

```html
<!DOCTYPE html>
<html lang="en">
<head>
<meta charset="utf-8">
<title>Bright Path Foundation</title>
<link rel="stylesheet" href="https://fonts.googleapis.com/css2?family=Cinzel:wght@400;700&family=Poppins:ital,wght@0,400;0,500;1,400&display=swap">
<style>
:root{
  --purple:#8a63b3;
  --purple-dark:#6f4a9c;
  --green:#8dc63f;
  --green-dark:#76ad2c;
  --ink:#222;
  --text:#666;
  --light:#f3f3f3;
  --black:#0d0d0d;
  --white:#fff;
}
*{box-sizing:border-box;margin:0;padding:0}
html,body{width:1200px;height:3625px;overflow:hidden}
body{position:relative;background:var(--white);font-family:"Poppins",sans-serif;color:var(--text)}
.abs{position:absolute}
.serif{font-family:"Cinzel",serif}

/* top bar */
.topbar{left:369px;top:0;width:689px;height:35px;background:var(--purple);clip-path:polygon(22px 0,100% 0,100% 100%,0 100%);color:#fff;font-size:13px}
.topbar span{position:absolute;top:8px;display:flex;align-items:center;gap:8px}
.donate{left:922px;top:0;width:136px;height:35px;background:var(--green);color:#fff;font-size:14px;display:flex;align-items:center;justify-content:center;gap:8px}
.logo{left:140px;top:44px;display:flex;align-items:center;gap:10px}
.logo-dot{width:30px;height:30px;border-radius:50%;background:var(--purple)}
.logo-name{font-family:"Cinzel",serif;color:var(--purple);font-size:21px;line-height:1.05}
.nav{left:426px;top:60px;display:flex;gap:0}
.nav a{position:absolute;white-space:nowrap;font-family:"Cinzel",serif;font-size:15px;color:var(--ink);text-decoration:none}
.nav a.active{color:var(--green)}
.search{left:1031px;top:57px;width:27px;height:27px;border-radius:50%;background:var(--purple)}

/* hero */
.hero{left:0;top:105px;width:1200px;height:625px;background:linear-gradient(100deg,#3e2f25 0%,#6a4a30 35%,#8a5a2c 55%,#5b4a3a 80%,#3a2f28 100%)}
.hero-title{left:0;top:283px;width:1200px;text-align:center;color:#fff;font-family:"Cinzel",serif;font-weight:700;font-size:70px;line-height:80px}
.hero-sub{left:320px;top:452px;width:560px;text-align:center;color:#fff;font-family:"Cinzel",serif;font-weight:700;font-size:14.5px;line-height:21px}
.arrow{width:34px;height:34px;border-radius:50%;display:flex;align-items:center;justify-content:center}

/* section titles */
.sec-title{font-family:"Cinzel",serif;font-size:34px;color:var(--purple);white-space:nowrap}
.sec-title .g{color:var(--green)}

.about-text{left:610px;top:877px;width:450px;text-align:center;font-size:12.6px;line-height:21.7px}
.btn{border-radius:18px;background:var(--green);color:#fff;font-family:"Cinzel",serif;font-weight:700;font-size:13px;display:flex;align-items:center;justify-content:center}

/* projects */
.projects-bg{left:0;top:1265px;width:1200px;height:655px;background:var(--light)}
.card{top:1489px;width:211px;height:291px}
.card .photo{height:151px}
.card .body{height:140px;color:#fff;text-align:center;padding-top:28px}
.card h3{font-family:"Cinzel",serif;font-weight:700;font-size:15px;line-height:20px}
.card p{font-size:12.6px;line-height:22px;margin-top:6px}
.card .plus{position:absolute;left:91px;bottom:-14px;width:29px;height:29px;border-radius:50%;background:#fff;border:1px solid #ddd;color:var(--purple);font-size:15px;display:flex;align-items:center;justify-content:center}
.purple{background:var(--purple)}
.green{background:var(--green)}

/* testimonial */
.quote{left:387px;top:2082px;width:570px;font-size:11px;line-height:19px;font-style:italic;color:#444}
.avatar{left:222px;top:2071px;width:136px;height:136px;border-radius:50%;border:7px solid #ddd;background:linear-gradient(160deg,#f1e3d6,#c9a78c)}

/* get involved */
.involved-bg{left:0;top:2343px;width:1200px;height:464px;background:var(--green)}
.involved-right{left:790px;top:2343px;width:410px;height:464px;background:var(--light)}
.involve-item{left:141px;display:flex;align-items:center;gap:14px;color:#fff;font-family:"Cinzel",serif;font-weight:700;font-size:15px}
.involve-item i{width:48px;height:48px;border-radius:50%;background:#fff;display:block}

/* newsletter */
.field{height:34px;border:1px solid #ccc;background:#fff;font-size:12.5px;color:#444;padding:9px 12px}

/* footer */
.footer{left:0;top:3200px;width:1200px;height:425px;background:var(--black)}
.f-head{font-family:"Cinzel",serif;font-size:17px;color:#fff;padding-bottom:10px;border-bottom:1px solid #444}
.f-links li{list-style:none;color:#fff;font-size:13px;margin-bottom:12px;display:flex;align-items:center;gap:10px}
.f-links li::before{content:"";width:4px;height:4px;border-radius:50%;background:#aaa}
.f-links li.active{color:var(--green)}
.f-contact{display:flex;gap:12px;color:#fff;font-size:13px;line-height:18px;align-items:flex-start}
.f-contact i{flex:none;width:32px;height:32px;border-radius:50%;border:1px solid #888;display:flex;align-items:center;justify-content:center}
.f-field{left:653px;width:183px;background:#fff;font-size:10px;color:#444;padding:6px 8px}
.copyright{left:0;top:3594px;width:1200px;text-align:center;color:#ddd;font-size:13px}
</style>
</head>
<body>

<!-- header -->
<div class="abs topbar">
  <span style="left:53px"><svg width="20" height="20" viewBox="0 0 20 20"><circle cx="10" cy="10" r="10" fill="#fff"/><path d="M7 5l2 2-1 2 3 3 2-1 2 2-2 2C9 15 5 11 5 7z" fill="#8a63b3"/></svg>(123) 456 7890</span>
  <span style="left:215px"><svg width="20" height="20" viewBox="0 0 20 20"><circle cx="10" cy="10" r="10" fill="#fff"/><rect x="5" y="6.5" width="10" height="7" fill="#8a63b3"/><path d="M5 6.5l5 4 5-4" stroke="#fff" fill="none"/></svg>info@brightpathfdn.org</span>
</div>
<div class="abs donate">Donate Now <svg width="8" height="10"><path d="M0 0l8 5-8 5z" fill="#fff"/></svg></div>

<div class="abs logo"><span class="logo-dot"></span><span class="logo-name">Bright Path<br>Foundation</span></div>

<nav class="abs nav">
  <a class="active" style="left:0">Home</a>
  <a style="left:85px">About Us</a>
  <a style="left:199px">Projects</a>
  <a style="left:307px">Get Involved ▾</a>
  <a style="left:465px">Contact Us</a>
</nav>
<svg class="abs" style="left:445px;top:80px" width="8" height="8"><circle cx="4" cy="4" r="4" fill="#8dc63f"/></svg>
<div class="abs search"><svg width="27" height="27"><circle cx="12.5" cy="12.5" r="4" stroke="#fff" stroke-width="1.6" fill="none"/><path d="M15.5 15.5l3 3" stroke="#fff" stroke-width="1.6"/></svg></div>

<!-- hero -->
<div class="abs hero" role="img" aria-label="Photo of smiling villagers, a man, a woman and a child, outside a thatched hut"></div>
<h1 class="abs hero-title">Bright Path<br>Foundation</h1>
<p class="abs hero-sub">Lorem ipsum dolor sit amet, consectetuer adipiscing elit, sed diam nonummy nibh euismod tincidunt ut laoreet dolore magna aliquam erat</p>
<div class="abs arrow" style="left:67px;top:388px;background:#fff"><svg width="10" height="12"><path d="M7 1L2 6l5 5" stroke="#333" stroke-width="2" fill="none"/></svg></div>
<div class="abs arrow" style="left:1109px;top:388px;background:var(--purple)"><svg width="10" height="12"><path d="M3 1l5 5-5 5" stroke="#fff" stroke-width="2" fill="none"/></svg></div>
<svg class="abs" style="left:0;top:590px" width="1200" height="145" viewBox="0 0 1200 145">
  <path d="M0 60 C200 0 420 10 620 60 S980 140 1200 95 L1200 145 L0 145Z" fill="#fff"/>
  <path d="M0 60 C200 0 420 10 620 60 C500 30 250 25 0 85Z" fill="#8dc63f"/>
  <path d="M520 40 C700 60 820 120 1000 130 C1100 135 1160 115 1200 95 L1200 110 C1100 140 960 145 800 120 C700 105 620 60 520 40Z" fill="#8a63b3"/>
</svg>

<!-- about -->
<svg class="abs" style="left:140px;top:780px" width="460" height="415" viewBox="0 0 460 415" role="img" aria-label="Heart-shaped photo of a smiling woman in a bright traditional hat with a small child">
  <defs><linearGradient id="aboutg" x1="0" y1="0" x2="1" y2="1"><stop offset="0" stop-color="#5a3a32"/><stop offset=".45" stop-color="#c9833a"/><stop offset="1" stop-color="#6d4a8c"/></linearGradient></defs>
  <path d="M230 395 C120 310 10 230 10 120 C10 50 60 5 120 5 C170 5 210 35 230 70 C250 35 290 5 340 5 C400 5 450 50 450 120 C450 230 340 310 230 395Z" fill="url(#aboutg)"/>
</svg>
<h2 class="abs sec-title" style="left:728px;top:778px">About <span class="g">Us</span></h2>
<svg class="abs" style="left:737px;top:843px" width="194" height="14"><line x1="4" y1="7" x2="190" y2="7" stroke="#8dc63f"/><circle cx="4" cy="7" r="3" fill="#8dc63f"/><circle cx="190" cy="7" r="3" fill="#8dc63f"/><circle cx="97" cy="7" r="7" fill="#8a63b3"/></svg>
<p class="abs about-text">Lorem ipsum dolor sit amet, consectetuer adipiscing elit, sed diam nonummy nibh euismo d tincidunt ut laoreet dolore magna aliquam erat volutpat. Ut wisi enim ad minim veniam, quis nostrud exerci tation ullamcorper suscipit lobortis nisl ut aliquip ex ea commodo consequat. Duis autem vel eum iriure dolor in hendrerit in vulputate velit esse molestie consequat, vel illum dolore eu feugiat nulla facilisis at vero eros et accumsan et iusto odio dignissim qui blandit praesent luptatum zzril delenit augue duis dolore te feugait nulla facilisi.ullamcorper suscipit lobortis nisl ut aliquip ex ea commodo consequat. Duis autem vel eum iriure dolor in hendrerit in vulputate velit esse molestie consequat. facilisi.ullamcorper suscipit lobortis nisl ut aliquip ex ea commodo consequat.</p>
<div class="abs btn" style="left:771px;top:1165px;width:127px;height:33px">Read More</div>

<!-- projects -->
<div class="abs projects-bg"></div>
<svg class="abs" style="left:0;top:1265px" width="1200" height="90" viewBox="0 0 1200 90"><path d="M0 0 L1200 0 L1200 30 C950 90 700 70 500 30 C300 0 120 20 0 60Z" fill="#fff"/></svg>
<h2 class="abs sec-title" style="left:497px;top:1378px">Our <span class="g">Project</span></h2>
<svg class="abs" style="left:503px;top:1433px" width="194" height="14"><line x1="4" y1="7" x2="190" y2="7" stroke="#8dc63f"/><circle cx="4" cy="7" r="3" fill="#8dc63f"/><circle cx="190" cy="7" r="3" fill="#8dc63f"/><circle cx="97" cy="7" r="7" fill="#8a63b3"/></svg>

<div class="abs card" style="left:141px">
  <div class="photo" role="img" aria-label="Photo of a nurse with a stethoscope examining a boy" style="background:linear-gradient(135deg,#a86a4a,#3fa9d6)"></div>
  <div class="body purple"><h3>Lorem Ipsum<br>Dolor</h3><p>Lorem ipsum dolor sit amet,<br>consectetuer adipiscing elit,</p></div>
  <span class="plus">+</span>
</div>
<div class="abs card" style="left:377px">
  <div class="photo" role="img" aria-label="Photo of volunteers working in a green garden" style="background:linear-gradient(135deg,#3d6b2a,#c8462c)"></div>
  <div class="body green"><h3>Lorem Ipsum<br>Dolor</h3><p>Lorem ipsum dolor sit amet,<br>consectetuer adipiscing elit,</p></div>
  <span class="plus">+</span>
</div>
<div class="abs card" style="left:612px">
  <div class="photo" role="img" aria-label="Photo of young volunteers packing a donations box" style="background:linear-gradient(135deg,#8a6a48,#3a6fb8)"></div>
  <div class="body purple"><h3>Lorem Ipsum<br>Dolor</h3><p>Lorem ipsum dolor sit amet,<br>consectetuer adipiscing elit,</p></div>
  <span class="plus">+</span>
</div>
<div class="abs card" style="left:847px">
  <div class="photo" role="img" aria-label="Illustration of colourful hands around a globe" style="background:linear-gradient(135deg,#e9f3fb,#3aa0d8 55%,#8dc63f)"></div>
  <div class="body green"><h3>Lorem Ipsum<br>Dolor</h3><p>Lorem ipsum dolor sit amet,<br>consectetuer adipiscing elit,</p></div>
  <span class="plus">+</span>
</div>
<div class="abs btn" style="left:537px;top:1815px;width:126px;height:34px">View All</div>

<!-- testimonial -->
<h2 class="abs sec-title" style="left:450px;top:1980px">Our <span class="g">Testimonial</span></h2>
<svg class="abs" style="left:503px;top:2035px" width="194" height="14"><line x1="4" y1="7" x2="190" y2="7" stroke="#8dc63f"/><circle cx="4" cy="7" r="3" fill="#8dc63f"/><circle cx="190" cy="7" r="3" fill="#8dc63f"/><circle cx="97" cy="7" r="7" fill="#8a63b3"/></svg>
<div class="abs avatar" role="img" aria-label="Portrait photo of a smiling client"></div>
<p class="abs quote"><b style="color:var(--purple);font-size:16px">“</b>Lorem ipsum dolor sit amet, consectetur adipiscing elit, sed do eiusmod tempor incididunt ut labore et dolore magna aliqua. Ut enim  veniam, quis nostrud exercitation ullamco laboris nisi ut aliquip ex ea commodo consequat. Duis aute irure dolor in reprehenderit in voluptate velit esse cillum dolore eu fugiat nulla pariatur. Excepteur sint occaecat cupidatat non proident, sunt in culpa qui officia.<b style="color:var(--purple);font-size:16px">”</b></p>
<svg class="abs" style="left:340px;top:2180px" width="610" height="30"><path d="M0 10 L600 6 L560 10 L548 24 L520 10Z" fill="none" stroke="#ddd"/></svg>
<p class="abs" style="left:680px;top:2197px;font-size:13px;font-style:italic;font-weight:500;color:#333">-Company Name</p>
<p class="abs" style="left:722px;top:2217px;font-size:12px;color:var(--green);letter-spacing:2px">★★★★★</p>
<svg class="abs" style="left:540px;top:2268px" width="40" height="8"><circle cx="4" cy="4" r="3.5" fill="#8dc63f"/><circle cx="18" cy="4" r="3" fill="#ccc"/><circle cx="32" cy="4" r="3" fill="#ccc"/></svg>

<!-- get involved -->
<div class="abs involved-bg"></div>
<div class="abs involved-right"></div>
<svg class="abs" style="left:528px;top:2340px" width="545" height="470" viewBox="0 0 545 470" role="img" aria-label="Heart-shaped photo of women joining hands above a pink sign reading get involved">
  <defs><linearGradient id="invg" x1="0" y1="0" x2="1" y2="1"><stop offset="0" stop-color="#c3d8ea"/><stop offset=".5" stop-color="#d6509a"/><stop offset="1" stop-color="#e58cbc"/></linearGradient></defs>
  <path d="M272 465 C140 380 5 280 5 140 C5 55 65 3 140 3 C200 3 250 40 272 85 C294 40 344 3 404 3 C480 3 540 55 540 140 C540 280 405 380 272 465Z" fill="url(#invg)"/>
</svg>
<h2 class="abs sec-title" style="left:141px;top:2405px;color:#fff">Get Involved</h2>
<svg class="abs" style="left:141px;top:2459px" width="194" height="14"><line x1="4" y1="7" x2="190" y2="7" stroke="#fff"/><circle cx="4" cy="7" r="3" fill="#fff"/><circle cx="190" cy="7" r="3" fill="#fff"/><circle cx="97" cy="7" r="7" fill="#8a63b3"/></svg>
<p class="abs" style="left:141px;top:2500px;width:385px;color:#fff;font-size:12.6px;line-height:21.5px">Lorem ipsum dolor sit amet, consectetuer adipiscing elit, sed diam nonummy nibh euismo d tincidunt ut laoreet dolore magna aliquam erat volutpat.</p>
<div class="abs involve-item" style="top:2584px"><i></i>Give a Donation</div>
<div class="abs involve-item" style="top:2646px"><i></i>Volunteer</div>
<div class="abs involve-item" style="top:2707px"><i></i>Corporate Support</div>

<!-- newsletter -->
<h2 class="abs sec-title" style="left:450px;top:2862px;color:#111">Newsletter <span class="g">Signup</span></h2>
<svg class="abs" style="left:503px;top:2915px" width="194" height="14"><line x1="4" y1="7" x2="190" y2="7" stroke="#8dc63f"/><circle cx="4" cy="7" r="3" fill="#8dc63f"/><circle cx="190" cy="7" r="3" fill="#8dc63f"/><circle cx="97" cy="7" r="7" fill="#8a63b3"/></svg>
<svg class="abs" style="left:818px;top:2886px" width="50" height="32"><path d="M0 10 L48 2 L28 30 L22 16Z" fill="#8dc63f"/></svg>
<p class="abs" style="left:300px;top:2958px;width:600px;text-align:center;font-size:11.5px;line-height:19px;color:#444">Vivamus hendrerit rhoncus tincidunt. Aenean tincidunt urna vel erat porta mattis. Nam id dui at eros pharetra sollicitudin. Proin at quam blandit, porttitor lacus a, lacinia velit.</p>
<div class="abs field" style="left:267px;top:3014px;width:328px">Your Name</div>
<div class="abs field" style="left:605px;top:3014px;width:328px">Your Email</div>
<div class="abs" style="left:529px;top:3065px;width:141px;height:36px;background:var(--green);color:#fff;font-size:14px;display:flex;align-items:center;justify-content:center">SUBSCRIBE</div>

<!-- footer -->
<div class="abs footer"></div>
<svg class="abs" style="left:0;top:3130px" width="1200" height="150" viewBox="0 0 1200 150">
  <path d="M0 70 C300 -10 560 40 760 100 C950 150 1100 120 1200 80 L1200 150 L0 150Z" fill="#0d0d0d"/>
  <path d="M0 50 C300 -20 560 30 760 90 C600 50 300 20 0 70Z" fill="#8a63b3"/>
  <path d="M640 80 C800 130 1000 140 1200 70 L1200 85 C1000 150 800 140 640 80Z" fill="#8dc63f"/>
</svg>

<h3 class="abs f-head" style="left:142px;top:3338px;width:115px">Quick Links</h3>
<ul class="abs f-links" style="left:142px;top:3383px">
  <li class="active">Home</li><li>About Us</li><li>Projects</li><li>Get involved</li><li>Contact Us</li>
</ul>
<h3 class="abs f-head" style="left:359px;top:3338px;width:198px">Contact Details</h3>
<div class="abs f-contact" style="left:353px;top:3386px;width:200px"><i><svg width="12" height="16"><path d="M6 15C2 9 1 7 1 5.5a5 5 0 0110 0C11 7 10 9 6 15z" stroke="#fff" fill="none"/><circle cx="6" cy="5.5" r="1.6" fill="#fff"/></svg></i><span>Lorem ipsum dolor sit 1234, Lorem ipsum dolor sit amet.</span></div>
<div class="abs f-contact" style="left:353px;top:3453px"><i><svg width="14" height="14"><path d="M3 1l3 3-1.5 2 3.5 3.5 2-1.5 3 3-2 2C5 13 1 9 1 3z" stroke="#fff" fill="none"/></svg></i><span style="margin-top:7px">(123)456 7890</span></div>
<div class="abs f-contact" style="left:353px;top:3503px"><i><svg width="14" height="10"><rect x=".5" y=".5" width="13" height="9" stroke="#fff" fill="none"/><path d="M.5 .5l6.5 5 6.5-5" stroke="#fff" fill="none"/></svg></i><span style="margin-top:7px">info@brightpathfdn.org</span></div>
<h3 class="abs f-head" style="left:653px;top:3334px;width:186px">Quick <span style="color:var(--green)">Contact</span></h3>
<div class="abs f-field" style="top:3388px;height:26px">Your Name</div>
<div class="abs f-field" style="top:3424px;height:26px">Your Email</div>
<div class="abs f-field" style="top:3460px;height:41px">Message</div>
<div class="abs" style="left:653px;top:3512px;width:93px;height:26px;background:var(--green);color:#fff;font-size:12px;display:flex;align-items:center;justify-content:center;gap:6px">SUBMIT <svg width="16" height="8"><path d="M0 4h14M11 1l3 3-3 3" stroke="#fff" fill="none"/></svg></div>
<div class="abs" style="left:890px;top:3380px;width:180px;display:flex;flex-direction:column;align-items:center;gap:12px">
  <span style="width:64px;height:64px;border-radius:50%;background:var(--purple)"></span>
  <span style="font-family:'Cinzel',serif;color:var(--purple);font-size:20px;text-align:center;line-height:1.1">Bright Path<br>Foundation</span>
</div>
<p class="abs copyright">Copyright  2019 Bright Path. All Rights Reserved.</p>

</body>
</html>
```